Etiketten für zwei neue Weinschorlen
Zielgruppe
Zielgruppe sind junge Leute, die gerne eine Erfrischung für unterwegs kaufen möchten
Hallo zusammen,
wir sind ein Familienweingut aus Mainfranken und möchten für einen Großkunden zwei neue Weinschorlen abfüllen. Dafür benötigen wir zwei Etiketten
Geplant sind eine Silvaner-Schorle und eine Rotling-Schorle.
Diese beiden Begriffe sind der jeweilige Artikelname und müssen zwingend auf das Etikett
Für beide gilt: die Schorle soll in einer 0,275 l Flasche mit Kronkorken, pfandfrei angeboten werden.
Die Farbe des Verschlusses ist noch nicht festgelegt. Wir können diese passend zum Etikett später noch anpassen.
Wir haben von einem befreundeten Weingut ein schönes Etikett erhalten, welches wir als Beispiel verwenden dürfen, um zu zeigen, in welche Stilrichtung das Etikett gehen soll. Bitte an diesem Etikett orientieren, NICHT am Wolkenspritz Etikett.
Ebenso haben wir hier eine Abbildung einer bereits abgefüllten kleinen Schorle als Beispiel, wie die Flasche am Ende ungefähr aussieht. Bei der Flasche handelt es sich allerdings um eine 0,33 l Flasche, das ist also nur ein grober Richtwert.
Wir benötigen am Ende eine Datei in Adobe Illustrator oder InDesign.
Die Abmessungen jedes Etiketts sollen 140 x 50 mm sein.
Uns geht es hauptsächlich um die Gestaltung des Bildes. Dieses soll 10 cm breit und 5 cm hoch sein.
Die Daten auf der rechten Seite (dieser Bereich soll bitte 4 cm breit sein) bitte einfach 1:1 übernehmen oder mit einem Blindtext ausfüllen, damit wir diese später mit den korrekten Angaben überschreiben können. Wir müssen hier gesetzliche Vorgaben was die Schriftgröße oder Größe des QR-Codes angeht einhalten.
Wir freuen uns auf Eure Vorschläge

```html
<!DOCTYPE html>
<html lang="de">
<head>
<meta charset="utf-8">
<title>Weinschorle Etiketten</title>
<link rel="stylesheet" href="https://fonts.googleapis.com/css2?family=Fira+Sans:wght@400&family=Montserrat:wght@800&display=swap">
<style>
  :root {
    --page-bg: #ffffff;
    --silvaner-title: #4a93b8;
    --rotling-title: #a8285a;
    --text-dark: #1c1c1c;
    --sky-light: #e6f0fb;
    --sky: #c6dcf3;
    --meadow: #d2e5cf;
    --sun: #fcf7c6;
    --lavender: #cdc9e8;
    --lavender-light: #eceaf7;
    --bottle: #b9a9e0;
    --silvaner-splash: #f2d84a;
    --silvaner-splash-deep: #e4b53a;
    --rotling-splash: #e79aa6;
    --rotling-splash-deep: #c93a5c;
    --silvaner-panel: #fbf6a6;
    --rotling-panel: #efd3c5;
    --code-box: #ffffff;
  }
  * { margin: 0; padding: 0; box-sizing: border-box; }
  html, body { width: 846px; height: 1200px; overflow: hidden; background: var(--page-bg); }
  .sheet { position: relative; width: 846px; height: 1200px; }

  .label {
    position: absolute;
    left: 70px;
    width: 714px;
    display: flex;
    box-shadow: 0 4px 8px rgba(0,0,0,0.18);
  }
  .label--silvaner { top: 69px; height: 273px; }
  .label--rotling { top: 392px; height: 267px; }

  .label__art {
    position: relative;
    width: 502px;
    height: 100%;
    overflow: hidden;
  }
  .art__landscape, .art__scene {
    position: absolute;
    inset: 0;
    width: 100%;
    height: 100%;
  }
  .label__title {
    position: absolute;
    left: 32px;
    top: 28px;
    font-family: "Montserrat", sans-serif;
    font-weight: 800;
    font-size: 42px;
    line-height: 52px;
    letter-spacing: 0.5px;
  }
  .label--silvaner .label__title { color: var(--silvaner-title); }
  .label--rotling .label__title { color: var(--rotling-title); }

  .label__info {
    position: relative;
    flex: 1;
    padding: 30px 12px 0 12px;
    font-family: "Fira Sans", sans-serif;
    color: var(--text-dark);
  }
  .label--silvaner .label__info { background: linear-gradient(90deg, #fffef6 0%, var(--silvaner-panel) 100%); }
  .label--rotling .label__info { background: linear-gradient(90deg, #fdf8f5 0%, var(--rotling-panel) 100%); }

  .info__slogan { font-size: 15px; line-height: 18px; }
  .info__name { font-size: 14.5px; line-height: 18px; margin-top: 11px; letter-spacing: 0.3px; }
  .info__desc { font-size: 10.2px; line-height: 12.8px; margin-top: 4px; }
  .info__volume {
    position: absolute;
    right: 27px;
    top: 186px;
    font-size: 23px;
    line-height: 28px;
  }
  .info__box { position: absolute; background: var(--code-box); }
  .info__box--left { left: 11px; top: 205px; width: 52px; height: 42px; }
  .info__box--right { left: 115px; top: 219px; width: 70px; height: 29px; }
</style>
</head>
<body>
<main class="sheet">

  <section class="label label--silvaner">
    <div class="label__art">
      <svg class="art__landscape" viewBox="0 0 502 273" preserveAspectRatio="none" aria-hidden="true">
        <defs>
          <linearGradient id="sky-a" x1="0" y1="0" x2="1" y2="0.4">
            <stop offset="0" stop-color="var(--sky-light)"/>
            <stop offset="1" stop-color="var(--sky)"/>
          </linearGradient>
        </defs>
        <rect width="502" height="273" fill="url(#sky-a)"/>
        <path d="M0 66 C120 60 260 80 502 58 L502 273 L0 273 Z" fill="var(--meadow)"/>
        <path d="M0 110 C140 100 300 122 502 112 L502 273 L0 273 Z" fill="var(--sun)"/>
        <path d="M0 200 C150 190 320 196 502 168 L502 273 L0 273 Z" fill="var(--lavender)"/>
        <path d="M0 250 C170 244 330 252 502 236 L502 273 L0 273 Z" fill="var(--lavender-light)"/>
      </svg>
      <svg class="art__scene" viewBox="0 0 502 273" role="img" aria-label="Illustration: zwei springende Personen und eine lila Flasche, aus der gelbe Silvaner-Schorle spritzt">
        <defs>
          <linearGradient id="scene-a" x1="0" y1="1" x2="1" y2="0">
            <stop offset="0" stop-color="var(--silvaner-splash)"/>
            <stop offset="0.55" stop-color="var(--silvaner-splash-deep)"/>
            <stop offset="1" stop-color="var(--bottle)"/>
          </linearGradient>
        </defs>
        <path d="M372 0 L502 0 L502 150 L430 230 L360 273 L220 273 L160 250 L90 230 L70 170 L110 140 L240 130 L330 120 L320 60 Z" fill="url(#scene-a)" opacity="0.85"/>
      </svg>
      <h2 class="label__title">SILVANER<br>SCHORLE</h2>
    </div>
    <div class="label__info">
      <p class="info__slogan">„Slogan“</p>
      <p class="info__name">SILVANER-SCHORLE</p>
      <p class="info__desc">Weinhaltiges Getränk mit 5%<br>Weißwein und 49% Mineralwasser<br>mit Kohlensäure versetzt.</p>
      <p class="info__volume">0,275l</p>
      <div class="info__box info__box--left"></div>
      <div class="info__box info__box--right"></div>
    </div>
  </section>

  <section class="label label--rotling">
    <div class="label__art">
      <svg class="art__landscape" viewBox="0 0 502 267" preserveAspectRatio="none" aria-hidden="true">
        <defs>
          <linearGradient id="sky-b" x1="0" y1="0" x2="1" y2="0.4">
            <stop offset="0" stop-color="var(--sky-light)"/>
            <stop offset="1" stop-color="var(--sky)"/>
          </linearGradient>
        </defs>
        <rect width="502" height="267" fill="url(#sky-b)"/>
        <path d="M0 64 C120 58 260 78 502 56 L502 267 L0 267 Z" fill="var(--meadow)"/>
        <path d="M0 108 C140 98 300 120 502 110 L502 267 L0 267 Z" fill="var(--sun)"/>
        <path d="M0 196 C150 186 320 192 502 164 L502 267 L0 267 Z" fill="var(--lavender)"/>
        <path d="M0 245 C170 239 330 247 502 231 L502 267 L0 267 Z" fill="var(--lavender-light)"/>
      </svg>
      <svg class="art__scene" viewBox="0 0 502 267" role="img" aria-label="Illustration: zwei springende Personen und eine lila Flasche, aus der rosa Rotling-Schorle spritzt">
        <defs>
          <linearGradient id="scene-b" x1="0" y1="1" x2="1" y2="0">
            <stop offset="0" stop-color="var(--rotling-splash)"/>
            <stop offset="0.55" stop-color="var(--rotling-splash-deep)"/>
            <stop offset="1" stop-color="var(--bottle)"/>
          </linearGradient>
        </defs>
        <path d="M372 0 L502 0 L502 146 L430 225 L360 267 L220 267 L160 245 L90 225 L70 166 L110 137 L240 127 L330 117 L320 58 Z" fill="url(#scene-b)" opacity="0.85"/>
      </svg>
      <h2 class="label__title">ROTLING<br>SCHORLE</h2>
    </div>
    <div class="label__info">
      <p class="info__slogan">„Slogan“</p>
      <p class="info__name">ROTLING -SCHORLE</p>
      <p class="info__desc">Weinhaltiges Getränk mit 5%<br>Weißwein und 49% Mineralwasser<br>mit Kohlensäure versetzt.</p>
      <p class="info__volume">0,275l</p>
      <div class="info__box info__box--left"></div>
      <div class="info__box info__box--right"></div>
    </div>
  </section>

</main>
</body>
</html>
```